Webdesign für einen  Bauträger und Projektentwickler
Webdesign für einen Bauträger und Projektentwickler
Zielgruppe
Wir sind ein Bauträger und Projektentwickler aus Ulm. Kapitalanleger sind hauptsächlich unsere Zielgruppe.
Aufgabenstellung
Die bereits bestehende Webseite soll überarbeitet werden bzw. das Design & Layout soll modernisiert werden. Das Design soll edel und klassisch sein. Die Webseite soll Menschen anziehen, die wertige Immobilien oder Bauprojekte suchen. Das Design sollte bevorzugt mit dem Tool Adobe Photoshop erstellt werden. Das Unternehmenslogo wurde kürzlich überarbeitet, wurde jedoch noch nicht gelauncht. Dies soll mit der überarbeiteten Webseite geschehen.

```html
<!DOCTYPE html>
<html lang="de">
<head>
<meta charset="utf-8">
<title>Halden – Unsere Projekte</title>
<link rel="stylesheet" href="https://fonts.googleapis.com/css2?family=Work+Sans:wght@400;500;600&display=swap">
<style>
:root{
  --ink:#1b1b1b;
  --text:#3a3a3a;
  --muted:#777;
  --accent:#f2cd00;
  --panel:#f2f2f2;
  --band:#f7f7f7;
  --foot:#efefef;
  --white:#fff;
}
*{box-sizing:border-box;margin:0;padding:0}
html,body{width:1200px;height:2605px;overflow:hidden;background:var(--white)}
body{font-family:"Work Sans",sans-serif;color:var(--text);position:relative}
.wrap{position:absolute;left:235px;width:730px}
.underline{display:block;width:47px;height:3px;background:var(--accent);margin-top:10px}
.btn{display:inline-block;background:var(--accent);color:var(--ink);font-size:11px;font-weight:500;padding:12px 13px;text-decoration:none}
.ph{display:block}

/* header */
.header{position:absolute;top:0;left:0;width:1200px;height:86px}
.brand{position:absolute;left:235px;top:24px;display:flex;align-items:center;gap:9px}
.brand-mark{width:14px;height:14px;background:var(--accent)}
.brand-name{font-size:28px;font-weight:500;color:var(--ink);line-height:1}
.nav{position:absolute;right:235px;top:31px;display:flex;gap:29px}
.nav a{font-size:12px;font-weight:500;color:var(--ink);text-decoration:none;position:relative}
.nav a.active::after{content:"";position:absolute;left:0;bottom:-8px;width:46px;height:3px;background:var(--accent)}

.hero{position:absolute;top:86px;left:0;width:1200px;height:247px;background:linear-gradient(90deg,#dfe3e8 0%,#c9cdd0 25%,#6e8a55 45%,#a9b98a 55%,#e7e8ec 75%,#f4f5f7 100%)}

.crumbs{top:356px;font-size:11px;display:flex;gap:10px;align-items:center}
.crumbs .prev{color:var(--muted)}
.crumbs .cur{color:var(--ink);font-weight:500}

.h1{top:400px;font-size:26px;font-weight:500;color:var(--ink)}
.intro{top:464px;width:600px;font-size:11px;line-height:13px}
.h2{font-size:19px;font-weight:500;color:var(--ink)}

.plan{top:596px;height:236px;display:flex}
.plan-text{width:433px;background:var(--panel);padding:34px 40px}
.plan-text h3{font-size:17px;font-weight:500;color:var(--ink)}
.plan-text p{font-size:10.5px;line-height:17px;margin:16px 0 14px}
.plan-img{width:297px;background:linear-gradient(135deg,#3a5f99 0%,#7d9cc4 40%,#c9b46e 60%,#43546a 100%)}

.grid{display:grid;grid-template-columns:359px 359px;column-gap:12px;row-gap:20px}
.card{background:var(--panel);height:507px;padding:22px 27px;position:relative}
.card h3{font-size:17px;font-weight:500;color:var(--ink)}
.card .ph{width:306px;height:181px;margin-top:22px}
.card .lead{font-size:10.5px;line-height:17px;color:var(--ink);margin-top:20px;font-weight:500}
.card .body{font-size:10.5px;line-height:17px;margin-top:6px}
.card .btn{position:absolute;left:27px;top:443px}
.img-a{background:linear-gradient(180deg,#9fc3e6 0%,#e9ecef 45%,#a7a9a2 75%,#4f6a3b 100%)}
.img-b{background:linear-gradient(180deg,#9aa27f 0%,#6c7a89 40%,#d8dadc 70%,#8b8b8b 100%)}
.img-c{background:linear-gradient(180deg,#a9c5e1 0%,#e6ddd0 40%,#cfc3b2 75%,#6f7d60 100%)}

.quotes{position:absolute;top:1997px;left:0;width:1200px;height:355px;background:var(--band)}
.quotes h2{position:absolute;left:235px;top:45px;font-size:24px;line-height:29px;font-weight:500;color:var(--ink)}
.quotes .underline{position:absolute;left:235px;top:110px;margin:0}
.arrows{position:absolute;left:235px;top:232px;display:flex;gap:6px}
.arrows span{width:30px;height:30px;border-radius:50%;display:flex;align-items:center;justify-content:center;background:#ececec}
.arrows span.next{background:var(--accent)}
.quote{position:absolute;left:482px;top:46px;width:483px;font-size:10.5px;line-height:17px}
.quote p+p{margin-top:17px}
.rating{position:absolute;left:482px;top:253px;width:483px;display:flex;justify-content:space-between;font-size:9px}
.rating em{font-size:7.5px;color:var(--text)}
.stars{letter-spacing:1px;color:var(--ink)}

.footer{position:absolute;top:2352px;left:0;width:1200px;height:193px;background:var(--foot)}
.footer .brand{top:28px}
.foot-about{position:absolute;left:235px;top:86px;width:245px;font-size:10.5px;line-height:17px}
.foot-col{position:absolute;top:44px;font-size:10.5px;line-height:17px}
.foot-col h4{font-size:10.5px;font-weight:600;color:var(--ink);margin-bottom:9px}
.foot-col a{color:var(--text);text-decoration:none;display:block}
.ico{display:inline-block;vertical-align:-1px;margin-right:5px}
.bottom{position:absolute;top:2545px;left:0;width:1200px;height:60px}
.legal{position:absolute;left:235px;top:24px;font-size:10.5px}
.bottom .stars-line{position:absolute;left:533px;top:23px;font-size:9px}
.social{position:absolute;right:235px;top:14px;display:flex;gap:8px}
.social span{width:24px;height:24px;border-radius:50%;background:var(--accent)}
</style>
</head>
<body>

<header class="header">
  <div class="brand">
    <span class="brand-mark"></span>
    <span class="brand-name">Halden</span>
  </div>
  <nav class="nav">
    <a class="active" href="#">Projekte</a>
    <a href="#">Halden Gruppe</a>
    <a href="#">Immobilien-Blog</a>
    <a href="#">Aktuelles</a>
    <a href="#">Kontakt</a>
  </nav>
</header>

<div class="hero ph" role="img" aria-label="Foto einer modernen Wohnanlage mit Balkonen und begrüntem Innenhof"></div>

<div class="wrap crumbs"><span class="prev">Startseite</span>
  <svg width="12" height="8" viewBox="0 0 12 8"><path d="M0 4h10M7 1l3 3-3 3" stroke="#1b1b1b" stroke-width="1.3" fill="none"/></svg>
  <span class="cur">Projekte</span></div>

<div class="wrap h1">Unsere Projekte<span class="underline"></span></div>

<p class="wrap intro">Bei der Halden Gruppe ist kein Immobilien-Projekt ist wie das andere. Die Grundstücksauswahl erfolgt sorgfältig im Hinblick auf eine attraktive Lage. Bei der Planung der Gebäude legen wir großen Wert auf moderne Energetik und anspruchsvolle Architektur.</p>

<h2 class="wrap h2" style="top:556px">Bauvorhaben</h2>

<section class="wrap plan">
  <div class="plan-text">
    <h3>Projekte in Planung</h3><span class="underline"></span>
    <p>Wir haben bereits weitere Projekte in Planung. Wenn Sie an Informationen über zukünftige Objekte interessiert sind oder sich bereits vormerken lassen wollen, dann nehmen Sie einfach Kontakt mit uns auf. Wir freuen uns über Ihr Interesse.</p>
    <a class="btn" href="#">Kontakt aufnehmen</a>
  </div>
  <div class="plan-img ph" role="img" aria-label="Foto einer Glasfassade von unten gesehen"></div>
</section>

<h2 class="wrap h2" style="top:870px">Neubauwohnungen</h2>

<section class="wrap grid" style="top:913px">
  <article class="card">
    <h3>Lindenhöfe Erbach</h3><span class="underline"></span>
    <div class="ph img-a" role="img" aria-label="Visualisierung eines hellen Mehrfamilienhauses mit Balkonen"></div>
    <p class="lead">Das spannende Neubau-Ensemble umfasst drei Mehrfamilienhäuser, die Moderne und Tradition vereinen.</p>
    <p class="body">Unter klassischen Sparrendächern beherbergen geschmackvoll ausgestaltete Außenfassaden mit großzügigen Balkonen insgesamt 39 Wohnungen in verschiedenen Größen. Die großzügige Unterkellerung des Komplexes birgt ausreichend Fläche für Abstellräume, PKW- und Fahrradstellplätze.</p>
    <a class="btn" href="#">Details ansehen</a>
  </article>
  <article class="card">
    <h3>Vireo, Lettenwald</h3><span class="underline"></span>
    <div class="ph img-b" role="img" aria-label="Luftaufnahme zweier Mehrfamilienhäuser mit Parkplätzen"></div>
    <p class="lead">Das Objekt Vireo in Ulm-Böfingen besteht aus zwei Mehrfamilienhäusern mit insgesamt 22 Wohnungen und einer gemeinsamen Tiefgarage.</p>
    <p class="body">Die Wohnanlage liegt in der Bellmer-Allee - benannt nach Ansgar Bellmer (*13.05.1922, † 01.09.1991), einem der prägendsten deutschen Grafikdesigner des 20. Jahrhunderts.</p>
    <a class="btn" href="#">Details ansehen</a>
  </article>
  <article class="card">
    <h3>BH14 Leonberg</h3><span class="underline"></span>
    <div class="ph img-a" role="img" aria-label="Visualisierung eines Neubaus mit Balkonen und Garten"></div>
    <p class="lead">In exklusiver und exponierter Lage erstellen wir für Sie dieses kleine, hochwertige Neubauvorhaben in der „Unteren Burghalde“. Sie gilt als eine der besten Lagen in Leonberg</p>
    <p class="body">Die moderne Architektur der vier exklusiven Einheiten fügt sich harmonisch in die bestehende Bebauung ein. Das Umfeld ist geprägt von freistehenden Einfamilienhäusern und stilvollen Villen.</p>
    <a class="btn" href="#">Details ansehen</a>
  </article>
  <article class="card">
    <h3>Ära 1890</h3><span class="underline"></span>
    <div class="ph img-c" role="img" aria-label="Foto eines denkmalgeschützten Altbaus mit Sandsteinfassade"></div>
    <p class="lead" style="font-weight:400">&nbsp;- VERKAUFT -</p>
    <p class="body" style="margin-top:8px">Ein denkmalgeschütztes, herrschaftliches Anwesen kombiniert mit vollendet moderner Wohnarchitektur. 60 Wohnungen, hell und großzügig geschnitten, alte Werte und frische Akzente stilvoll realisiert und geschickt vereint.</p>
    <a class="btn" href="#">Details ansehen</a>
  </article>
</section>

<section class="quotes">
  <h2>Was unsere<br>Kunden sagen</h2>
  <span class="underline"></span>
  <div class="arrows">
    <span><svg width="10" height="12" viewBox="0 0 10 12"><path d="M7 1L2 6l5 5" stroke="#1b1b1b" stroke-width="2" fill="none"/></svg></span>
    <span class="next"><svg width="10" height="12" viewBox="0 0 10 12"><path d="M3 1l5 5-5 5" stroke="#fff" stroke-width="2" fill="none"/></svg></span>
  </div>
  <div class="quote">
    <p>"Bei der Zusammenarbeit im Zuge des Immobilienkaufs war ich bei der Halden Gruppe in besten Händen. Der Chef kümmerte sich persönlich um meine Anfragen, auch wenn es um Details ging. Ich konnte z.B. andere Türen wählen, als die, die zunächst angeboten waren. Meine Wünsche sind immer freundlich, pünktlich und zuvorkommend umgesetzt worden – das war eine positive Erfahrung! Um es auf den Punkt zu bringen: Das Gesamtpaket aus Preis, Leistung und Service hat einfach gestimmt!</p>
    <p>Über diese Professionalität hinaus finde ich auch die soziale Einstellung der Firma toll! Mit ihrer Initiative "Schritte für Kinder" sammelt die Halden Gruppe Spendengelder für soziale Einrichtungen in Ulm. Klar, dass auch ich jedes Jahr mit am Start bin und so das Engagement des Bauträgers unterstütze."</p>
  </div>
  <div class="rating"><span><span class="stars">★★★★★</span>&nbsp; 5 von 5 Sternen</span><em>Luca Verani, Selbstnutzer, 3-Zimmer-Wohnung, 78m²</em></div>
</section>

<footer class="footer">
  <div class="brand">
    <span class="brand-mark"></span>
    <span class="brand-name">Halden</span>
  </div>
  <p class="foot-about">Seit vielen Jahren schaffen wir nicht nur Gebäude. Als Bauträger haben wir, die Halden Gruppe, es uns zur Aufgabe gemacht, Ihre Wohnträume zu verwirklichen und einzigartige Investitionsobjekte zu schaffen.</p>
  <div class="foot-col" style="left:608px">
    <h4>Kontakt</h4>
    Halden Gruppe<br>Kornweg 12<br>89075 Ulm
    <div style="margin-top:6px"><svg class="ico" width="9" height="9" viewBox="0 0 10 10"><path d="M2 0l2 2.5-1.2 1.2a6 6 0 003.5 3.5L7.5 6 10 8l-1.5 2C4 10 0 6 0 1.5z" fill="#3a3a3a"/></svg>0171 000 2846<br>
    <svg class="ico" width="9" height="7" viewBox="0 0 10 7"><rect width="10" height="7" fill="#3a3a3a"/><path d="M0 0l5 4 5-4" stroke="#efefef" fill="none"/></svg>info@hofkarsp.de</div>
  </div>
  <div class="foot-col" style="left:792px">
    <h4>Menü</h4>
    <a href="#">Startseite</a><a href="#">Projekte</a><a href="#">Halden Gruppe</a><a href="#">Immobilien-Blog</a><a href="#">Aktuelles</a>
  </div>
</footer>

<div class="bottom">
  <div class="legal">Impressum | Datenschutz | AGB</div>
  <div class="stars-line"><span class="stars">★★★★★</span>&nbsp; 4,8 von 5 Sternen</div>
  <div class="social"><span></span><span></span><span></span></div>
</div>

</body>
</html>
```